Design a Travel and Tourism website

We would like a freelancer to design a website that is essentially easy to use and navigate database providing local information for Travelers about destination countries.

We proposed website would discuss different rates, fees, visa requirement, resort locations, cheap flights, etc. This website should be elegant and modern. Our business name is wandrello.
Some reference websites are skelvanora.ca, quorbelfindshop.com,
There should be a forum in the website where travell\ers discuss about their first hand tranvel experience to such destinations.

```html
<!DOCTYPE html>
<html lang="en">
<head>
<meta charset="utf-8">
<title>Wandrello – Find the perfect deals</title>
<link rel="stylesheet" href="https://fonts.googleapis.com/css2?family=Open+Sans:wght@400;600;700;800&family=Lato:wght@400;700&family=Dancing+Script:wght@400;600&display=swap">
<style>
:root{
  --green:#9cc29f;
  --sand:#c9c39c;
  --ink:#2f3236;
  --white:#ffffff;
  --panel:rgba(38,42,42,.78);
  --tabbar:rgba(30,33,34,.85);
  --field:#ffffff;
  --footer:#1e2128;
  --footer-bottom:#171a1f;
  --footer-text:#b9bcc1;
  --side-panel:#efefef;
  --caption:rgba(28,36,38,.55);
}
*{box-sizing:border-box;margin:0;padding:0}
html,body{width:1200px;height:2387px;overflow:hidden;background:var(--white)}
body{position:relative;font-family:'Open Sans',sans-serif;color:var(--ink)}

/* hero */
.hero{position:absolute;left:0;top:0;width:1200px;height:900px;overflow:hidden}
.hero-photo{position:absolute;inset:0;background:
  radial-gradient(ellipse 420px 520px at 620px 560px,rgba(70,74,60,.55),transparent 70%),
  linear-gradient(180deg,#7d928c 0%,#6a807a 30%,#5f746b 55%,#7c8a6c 80%,#8f9a78 100%)}
.hero-curve{position:absolute;left:0;top:0}

.nav{position:absolute;left:0;top:0;width:1200px;height:90px}
.nav-burger{position:absolute;left:58px;top:33px;width:26px;height:22px}
.nav-burger span{display:block;height:4px;background:var(--white);margin-bottom:5px;border-radius:1px}
.nav-link{position:absolute;top:32px;font-family:'Dancing Script',cursive;font-size:17px;color:var(--white);transform:translateX(-50%);white-space:nowrap}
.brand{position:absolute;left:600px;top:18px;transform:translateX(-50%);font-family:'Open Sans',sans-serif;font-weight:600;font-size:36px;line-height:48px;color:var(--white);white-space:nowrap;letter-spacing:.5px}

.headline{position:absolute;left:0;top:244px;width:1200px;text-align:center;color:var(--white);font-weight:600;font-size:42px;line-height:54px;letter-spacing:1.5px}
.headline .accent-green{color:var(--green)}
.headline .accent-sand{color:var(--sand)}

.search{position:absolute;left:243px;top:401px;width:715px;height:288px;background:var(--panel)}
.search-tabs{position:absolute;left:0;top:0;width:715px;height:40px;background:var(--tabbar)}
.search-tab{position:absolute;top:0;height:40px;line-height:40px;font-size:14px;font-weight:600;color:var(--white);transform:translateX(-50%);letter-spacing:.5px}
.search-tab.is-active{left:0;width:145px;transform:none;text-align:center;background:var(--green)}
.field-label{position:absolute;font-size:13px;color:#e6e8e6;text-align:right;width:140px}
.field-input{position:absolute;height:27px;background:var(--field);border-radius:2px;font-size:11px;color:#9a9a9a;padding-left:20px;line-height:27px}
.field-select{position:absolute;height:27px;width:45px;background:var(--field);border-radius:2px;font-size:11px;color:#888;padding-left:8px;line-height:27px}
.field-select::after{content:"";position:absolute;right:6px;top:11px;border:5px solid transparent;border-top:6px solid #333}
.search-button{position:absolute;left:475px;top:209px;width:191px;height:46px;background:var(--green);color:var(--white);font-size:17px;line-height:46px;padding-left:74px}
.search-button svg{position:absolute;left:30px;top:12px}

/* sections */
.section-backdrop{position:absolute;left:0;top:930px;width:1200px;height:1120px;background:radial-gradient(circle at 600px 560px,rgba(0,0,0,.035) 0,rgba(0,0,0,.035) 520px,transparent 522px)}
.section-kicker{position:absolute;left:0;width:1200px;text-align:center;font-family:'Dancing Script',cursive;font-size:22px;color:var(--ink)}
.section-title{position:absolute;left:0;width:1200px;text-align:center;font-weight:800;font-size:35px;letter-spacing:1.5px;color:var(--ink)}

.carousel{position:absolute;left:0;width:1200px;height:318px}
.carousel-side{position:absolute;top:0;height:318px;background:var(--side-panel)}
.carousel-side.left{left:0;width:60px;border-radius:0 10px 10px 0}
.carousel-side.right{right:0;width:50px;border-radius:10px 0 0 10px}
.carousel-arrow{position:absolute;top:141px}
.card{position:absolute;top:0;width:355px;height:318px;overflow:hidden}
.card-photo{position:absolute;inset:0}
.card-caption{position:absolute;left:0;bottom:0;width:100%;height:86px;background:var(--caption);color:var(--white)}
.card-name{position:absolute;left:16px;top:3px;font-size:37px;font-weight:600;line-height:46px}
.card-price{position:absolute;left:20px;top:48px;font-size:18px;font-weight:600}
.card-expand{position:absolute;right:18px;bottom:10px}
.photo-coast{background:linear-gradient(160deg,#3d6d3b 0%,#5a8a4c 18%,#2aa7e0 40%,#19b9d8 60%,#1d6fb0 100%)}
.photo-market{background:linear-gradient(180deg,#1f3d8a 0%,#2c4f96 18%,#b48a5a 40%,#8e3a2a 65%,#2a1b1a 100%)}
.photo-fountain{background:linear-gradient(180deg,#2b2e68 0%,#6d5a3c 18%,#9a7a4a 45%,#6b5232 75%,#3b3226 100%)}

/* footer */
.footer{position:absolute;left:0;top:2064px;width:1200px;height:264px;background:var(--footer);font-family:'Lato',sans-serif}
.footer-col{position:absolute;top:41px}
.footer-heading{font-size:15px;font-weight:700;letter-spacing:1.5px;color:var(--green);margin-bottom:29px}
.footer-link{font-size:15px;color:var(--footer-text);letter-spacing:.6px;height:36px}
.footer-bottom{position:absolute;left:0;top:2328px;width:1200px;height:59px;background:var(--footer-bottom);font-family:'Lato',sans-serif}
.copyright{position:absolute;left:70px;top:21px;font-size:12px;color:var(--footer-text);letter-spacing:.4px}
.copyright span{text-decoration:underline}
.social{position:absolute;left:974px;top:19px;display:flex;gap:6px}
.social span{width:21px;height:21px;border-radius:50%;background:#8a8d92}
</style>
</head>
<body>

<header class="hero">
  <div class="hero-photo" role="img" aria-label="Hiker with a backpack standing on a misty mountain ridge"></div>
  <svg class="hero-curve" width="1200" height="900" viewBox="0 0 1200 900" aria-hidden="true">
    <path d="M0 780 Q600 964 1200 780 L1200 900 L0 900 Z" fill="#ffffff"/>
  </svg>

  <nav class="nav">
    <div class="nav-burger"><span></span><span></span><span></span></div>
    <span class="nav-link" style="left:197px">Home</span>
    <span class="nav-link" style="left:283px">Flights</span>
    <span class="nav-link" style="left:369px">Hotels</span>
    <span class="nav-link" style="left:452px">Cars</span>
    <span class="brand">wandrello</span>
    <span class="nav-link" style="left:780px">Travel Insurance</span>
    <span class="nav-link" style="left:912px">Travel Costs</span>
    <span class="nav-link" style="left:1018px">Forums</span>
  </nav>

  <h1 class="headline">FIND THE PERFECT <span class="accent-green">DEALS</span> FOR<br>YOUR PERFECT <span class="accent-sand">HOLIDAYS</span></h1>

  <form class="search">
    <div class="search-tabs">
      <span class="search-tab is-active">FLIGHTS</span>
      <span class="search-tab" style="left:212px">HOTELS</span>
      <span class="search-tab" style="left:352px">CARS</span>
      <span class="search-tab" style="left:500px">INSURANCE</span>
      <span class="search-tab" style="left:640px">EXTRAS</span>
    </div>
    <label class="field-label" style="left:-30px;top:80px">Depart from:</label>
    <div class="field-input" style="left:126px;top:75px;width:210px">City or airport</div>
    <label class="field-label" style="left:298px;top:80px">Depart date:</label>
    <div class="field-input" style="left:454px;top:75px;width:212px">DD/MM/YYYY</div>
    <label class="field-label" style="left:-30px;top:127px">Depart to:</label>
    <div class="field-input" style="left:126px;top:122px;width:210px">City or airport</div>
    <label class="field-label" style="left:298px;top:127px">Return date:</label>
    <div class="field-input" style="left:454px;top:122px;width:212px">DD/MM/YYYY</div>
    <label class="field-label" style="left:-30px;top:176px">Adults:</label>
    <div class="field-select" style="left:126px;top:171px">1</div>
    <label class="field-label" style="left:-30px;top:224px">Children:</label>
    <div class="field-select" style="left:126px;top:218px">5+</div>
    <div class="search-button">
      <svg width="22" height="22" viewBox="0 0 22 22" aria-hidden="true"><circle cx="9" cy="9" r="6.5" fill="none" stroke="#fff" stroke-width="3"/><line x1="14" y1="14" x2="20" y2="20" stroke="#fff" stroke-width="3.5" stroke-linecap="round"/></svg>
      SEARCH
    </div>
  </form>
</header>

<div class="section-backdrop" role="img" aria-label="Faint travel landmarks decoration behind the deals"></div>

<section>
  <p class="section-kicker" style="top:948px">everybody loves deals</p>
  <h2 class="section-title" style="top:970px">HOTTEST DEALS</h2>
  <div class="carousel" style="top:1068px">
    <div class="carousel-side left"></div>
    <div class="carousel-side right"></div>
    <svg class="carousel-arrow" style="left:14px" width="24" height="36" viewBox="0 0 24 36" aria-hidden="true"><path d="M19 4 L6 18 L19 32" fill="none" stroke="#8fb593" stroke-width="6"/></svg>
    <svg class="carousel-arrow" style="left:1166px" width="24" height="36" viewBox="0 0 24 36" aria-hidden="true"><path d="M5 4 L18 18 L5 32" fill="none" stroke="#8fb593" stroke-width="6"/></svg>
    <article class="card" style="left:60px"><div class="card-photo photo-coast" role="img" aria-label="Turquoise bay below green cliffs"></div><div class="card-caption"><h3 class="card-name">Casa Blanca</h3><p class="card-price">From 120$/person</p><svg class="card-expand" width="16" height="16" viewBox="0 0 16 16" aria-hidden="true"><path d="M1 1h5L1 6zM15 1v5L10 1zM1 15v-5l5 5zM15 15h-5l5-5zM3 3l10 10M13 3L3 13" fill="#fff" stroke="#fff" stroke-width="1.6"/></svg></div></article>
    <article class="card" style="left:427px"><div class="card-photo photo-market" role="img" aria-label="City square with a lit evening market"></div><div class="card-caption"><h3 class="card-name">Paris</h3><p class="card-price">From 120$/person</p><svg class="card-expand" width="16" height="16" viewBox="0 0 16 16" aria-hidden="true"><path d="M1 1h5L1 6zM15 1v5L10 1zM1 15v-5l5 5zM15 15h-5l5-5zM3 3l10 10M13 3L3 13" fill="#fff" stroke="#fff" stroke-width="1.6"/></svg></div></article>
    <article class="card" style="left:791px"><div class="card-photo photo-fountain" role="img" aria-label="Baroque fountain facade lit at dusk"></div><div class="card-caption"><h3 class="card-name">Rome</h3><p class="card-price">From 120$/person</p><svg class="card-expand" width="16" height="16" viewBox="0 0 16 16" aria-hidden="true"><path d="M1 1h5L1 6zM15 1v5L10 1zM1 15v-5l5 5zM15 15h-5l5-5zM3 3l10 10M13 3L3 13" fill="#fff" stroke="#fff" stroke-width="1.6"/></svg></div></article>
  </div>
</section>

<section>
  <p class="section-kicker" style="top:1467px">people trust other people</p>
  <h2 class="section-title" style="top:1489px">HOTTEST PLACES</h2>
  <div class="carousel" style="top:1587px">
    <div class="carousel-side left"></div>
    <div class="carousel-side right"></div>
    <svg class="carousel-arrow" style="left:14px" width="24" height="36" viewBox="0 0 24 36" aria-hidden="true"><path d="M19 4 L6 18 L19 32" fill="none" stroke="#8fb593" stroke-width="6"/></svg>
    <svg class="carousel-arrow" style="left:1166px" width="24" height="36" viewBox="0 0 24 36" aria-hidden="true"><path d="M5 4 L18 18 L5 32" fill="none" stroke="#8fb593" stroke-width="6"/></svg>
    <article class="card" style="left:60px"><div class="card-photo photo-coast" role="img" aria-label="Turquoise bay below green cliffs"></div><div class="card-caption"><h3 class="card-name">Casa Blanca</h3><p class="card-price">From 120$/person</p><svg class="card-expand" width="16" height="16" viewBox="0 0 16 16" aria-hidden="true"><path d="M1 1h5L1 6zM15 1v5L10 1zM1 15v-5l5 5zM15 15h-5l5-5zM3 3l10 10M13 3L3 13" fill="#fff" stroke="#fff" stroke-width="1.6"/></svg></div></article>
    <article class="card" style="left:427px"><div class="card-photo photo-market" role="img" aria-label="City square with a lit evening market"></div><div class="card-caption"><h3 class="card-name">Paris</h3><p class="card-price">From 120$/person</p><svg class="card-expand" width="16" height="16" viewBox="0 0 16 16" aria-hidden="true"><path d="M1 1h5L1 6zM15 1v5L10 1zM1 15v-5l5 5zM15 15h-5l5-5zM3 3l10 10M13 3L3 13" fill="#fff" stroke="#fff" stroke-width="1.6"/></svg></div></article>
    <article class="card" style="left:791px"><div class="card-photo photo-fountain" role="img" aria-label="Baroque fountain facade lit at dusk"></div><div class="card-caption"><h3 class="card-name">Rome</h3><p class="card-price">From 120$/person</p><svg class="card-expand" width="16" height="16" viewBox="0 0 16 16" aria-hidden="true"><path d="M1 1h5L1 6zM15 1v5L10 1zM1 15v-5l5 5zM15 15h-5l5-5zM3 3l10 10M13 3L3 13" fill="#fff" stroke="#fff" stroke-width="1.6"/></svg></div></article>
  </div>
</section>

<footer class="footer">
  <div class="footer-col" style="left:215px"><h4 class="footer-heading">SITE MAP</h4><p class="footer-link">Flights</p><p class="footer-link">Hotels</p><p class="footer-link">Cars</p><p class="footer-link">Solutions</p></div>
  <div class="footer-col" style="left:412px"><h4 class="footer-heading">RESOURCES</h4><p class="footer-link">Hotel Insurance</p><p class="footer-link">Extra Costs</p><p class="footer-link">Resort Locations</p><p class="footer-link">Cheap Flights</p></div>
  <div class="footer-col" style="left:667px"><h4 class="footer-heading">COMPANY</h4><p class="footer-link">About</p><p class="footer-link">Forums</p><p class="footer-link">Success Stories</p><p class="footer-link">Contact</p></div>
  <div class="footer-col" style="left:871px"><h4 class="footer-heading">SUPPORT</h4><p class="footer-link">Support Center</p><p class="footer-link">Community</p></div>
</footer>
<div class="footer-bottom">
  <p class="copyright">© Wandrello, Inc. <span>Terms</span> <span>Privacy Policy</span></p>
  <div class="social" aria-label="Social links"><span></span><span></span><span></span><span></span><span></span></div>
</div>

</body>
</html>
```